Dorsey K. Wendell Business Card

We need a business card for our company Dorsey K. Wendell Heating & Plumbing to be distributed to potential customers. It should follow the color scheme of our logo and have a modern upscale and masculine look.

The logo is attached and the info below should also be included:

5187 W. Cedar Brook Rd.
Brookvale, PA 17390

Russell T. Wendell
(717) 592-0817
russelltwendell@fernmail.net
dorseykwendell.net
PA #093148

Industry/Entity Type

Business

Contact Information for Business Card

5187 W. Cedar Brook Rd.
Brookvale, PA 17390

Russell T. Wendell
(717) 592-0817
russelltwendell@fernmail.net
dorseykwendell.net
PA #093148

Colors

Designer to choose colors to be used in the design.

Requirements
Must have
• Information above included

```html
<!DOCTYPE html>
<html lang="en">
<head>
<meta charset="utf-8">
<title>Dorsey K. Wendell Business Card</title>
<link href="https://fonts.googleapis.com/css2?family=Exo+2:wght@400;500;700&display=swap" rel="stylesheet">
<style>
  :root {
    --brand-blue: #0d4ea6;
    --brand-blue-dark: #0a3f8a;
    --brand-green: #a6ce39;
    --text-grey: #8a8d91;
    --paper: #ffffff;
    --backdrop: #d9d9d9;
  }
  * { box-sizing: border-box; margin: 0; padding: 0; }
  html, body {
    width: 1200px; height: 800px; overflow: hidden;
    background: var(--backdrop);
    font-family: "Exo 2", sans-serif;
  }
  .sheet {
    position: relative; width: 1200px; height: 800px;
    display: flex; align-items: center; justify-content: center; gap: 40px;
  }
  .card {
    position: relative; width: 540px; height: 309px; overflow: hidden;
    box-shadow: 0 6px 18px rgba(0,0,0,.18);
  }
  /* front */
  .card-front { background: var(--paper); }
  .wordmark { display: flex; align-items: center; gap: 12px; }
  .wordmark-square { width: 34px; height: 34px; background: var(--brand-blue); flex: none; }
  .wordmark-name {
    font-weight: 700; text-transform: uppercase; line-height: 1.05;
    color: var(--brand-blue);
  }
  .card-front .wordmark { position: absolute; left: 150px; top: 48px; }
  .card-front .wordmark-name { font-size: 22px; letter-spacing: .5px; }
  .details {
    position: absolute; left: 70px; top: 132px;
    display: flex; align-items: center;
  }
  .person { text-align: right; padding-right: 20px; }
  .person-name { color: var(--brand-blue); font-size: 17px; font-weight: 500; text-transform: uppercase; letter-spacing: .5px; }
  .person-title, .person-license { color: var(--text-grey); font-size: 13px; text-transform: uppercase; line-height: 1.35; }
  .divider { width: 2px; height: 66px; background: var(--brand-green); }
  .contacts { list-style: none; padding-left: 20px; }
  .contacts li {
    display: flex; align-items: center; gap: 10px;
    color: var(--text-grey); font-size: 13px; line-height: 1.6;
  }
  .contacts svg { width: 12px; height: 12px; flex: none; fill: var(--brand-blue); }
  .contacts .web-domain { color: var(--brand-blue); }
  .location {
    position: absolute; left: 70px; bottom: 36px;
    font-size: 13px; color: var(--text-grey);
  }
  .location-label { color: var(--brand-blue); }
  .band-blue { position: absolute; left: 0; bottom: 0; width: 300px; height: 9px; background: var(--brand-blue); }
  .band-green { position: absolute; right: 0; bottom: 0; width: 240px; height: 9px; background: var(--brand-green); }
  /* back */
  .card-back {
    background: linear-gradient(135deg, var(--brand-blue) 0%, var(--brand-blue-dark) 100%);
  }
  .card-back .wordmark { position: absolute; left: 112px; top: 112px; }
  .card-back .wordmark-square { width: 46px; height: 46px; background: var(--paper); }
  .card-back .wordmark-name { color: var(--paper); font-size: 28px; }
  .back-web {
    position: absolute; right: 44px; bottom: 34px;
    color: var(--paper); font-size: 14px; letter-spacing: 1px;
  }
</style>
</head>
<body>
<main class="sheet">
  <section class="card card-front" aria-label="Business card front">
    <div class="wordmark">
      <span class="wordmark-square"></span>
      <span class="wordmark-name">Dorsey K. Wendell<br>Heating &amp; Plumbing</span>
    </div>
    <div class="details">
      <div class="person">
        <p class="person-name">Russell T. Wendell</p>
        <p class="person-title">President</p>
        <p class="person-license">PA #093148</p>
      </div>
      <span class="divider"></span>
      <ul class="contacts">
        <li><svg viewBox="0 0 12 12" aria-hidden="true"><path d="M3 0h6a1 1 0 0 1 1 1v10a1 1 0 0 1-1 1H3a1 1 0 0 1-1-1V1a1 1 0 0 1 1-1zm0 1.5v8h6v-8z"/></svg>(717) 592-0817</li>
        <li><svg viewBox="0 0 12 12" aria-hidden="true"><path d="M0 2h12v8H0zm1 1v.3l5 3.2 5-3.2V3z"/></svg>russelltwendell@fernmail.net</li>
        <li><svg viewBox="0 0 12 12" aria-hidden="true"><circle cx="6" cy="6" r="6"/></svg><span>www.<span class="web-domain">dorseykwendell.net</span></span></li>
      </ul>
    </div>
    <p class="location"><span class="location-label">Location:</span> 5187 W. Cedar Brook Rd. Brookvale, PA 17390</p>
    <span class="band-blue"></span>
    <span class="band-green"></span>
  </section>

  <section class="card card-back" aria-label="Business card back">
    <div class="wordmark">
      <span class="wordmark-square"></span>
      <span class="wordmark-name">Dorsey K. Wendell<br>Heating &amp; Plumbing</span>
    </div>
    <p class="back-web">www.dorseykwendell.net</p>
  </section>
</main>
</body>
</html>
```